Loft Plan Studio New Business Card

I am opening a new division of my business. I am a high end interior designer, and the new business is writing specs for construction projects. It will be marketed to the VERY high end contractor, architects and realtors. The client will actually be the one who pays us and signs the agreement, but it will be the contractor, architect or realtor that will recommend us. I have attached my current card and our previous logo which is still used on some of our paperwork. I would like the new logo to be connected in some way to what we are currently using. We will need to have room on the card for a person's name. I'd like to omit the address as we might be moving the office soon. The web address is www.LoftPlanStudio.example. For this design, please use my name, Marisol Whitfield.

Target Market(s)

High End Luxury Contractors, Realtors and Architects

Industry/Entity Type

Residential Construction

Contact Information for Business Card

Loft Plan Studio, Phone: 555-304-2917, www.LoftPlanStudio.example , Marisol Whitfield

Font styles to use
Sans Serif

Colors
ec1f27

Requirements
Must have
• Some visual reference to my current card and logos. Use the colors submitted on the business card I attached.
Nice to have
• A visual reference to my current card and logos. Use the colors submitted on the card I attached.
Should not have
• A physical address

```html
<!DOCTYPE html>
<html lang="en">
<head>
<meta charset="utf-8">
<title>Loft Plan Studio – Business Card</title>
<link href="https://fonts.googleapis.com/css2?family=Open+Sans:wght@400;700&display=swap" rel="stylesheet">
<style>
  :root {
    --backdrop: #e9e6e2;
    --card: #ffffff;
    --accent: #8b3a22;
    --text: #6b6b6b;
    --shadow: rgba(0, 0, 0, 0.18);
  }
  html, body {
    margin: 0;
    width: 1200px;
    height: 1000px;
    overflow: hidden;
    background: var(--backdrop);
    font-family: "Open Sans", sans-serif;
  }
  .card {
    position: absolute;
    left: 100px;
    top: 201px;
    width: 1000px;
    height: 598px;
    background: var(--card);
    box-shadow: 0 6px 18px var(--shadow);
  }
  .brand {
    position: absolute;
    left: 62px;
    top: 232px;
    display: flex;
    align-items: center;
    gap: 18px;
  }
  .brand-square {
    width: 54px;
    height: 54px;
    background: var(--accent);
  }
  .brand-name {
    font-size: 34px;
    font-weight: 400;
    color: var(--text);
    letter-spacing: 1px;
    white-space: nowrap;
  }
  .contact {
    position: absolute;
    left: 547px;
    top: 202px;
  }
  .person-name {
    margin: 0 0 42px;
    font-size: 28px;
    font-weight: 700;
    color: var(--accent);
    text-transform: uppercase;
    letter-spacing: 0.3px;
  }
  .contact-list {
    list-style: none;
    margin: 0;
    padding: 0;
  }
  .contact-item {
    display: flex;
    align-items: center;
    gap: 12px;
    font-size: 24px;
    line-height: 36px;
    color: var(--text);
  }
  .contact-icon {
    width: 20px;
    height: 20px;
    fill: var(--accent);
    flex: none;
  }
</style>
</head>
<body>
  <div class="card">
    <div class="brand">
      <div class="brand-square"></div>
      <div class="brand-name">Loft Plan Studio</div>
    </div>

    <div class="contact">
      <h1 class="person-name">Marisol Whitfield</h1>
      <ul class="contact-list">
        <li class="contact-item">
          <svg class="contact-icon" viewBox="0 0 20 20" aria-hidden="true">
            <path d="M2 6c0-2 3-3 8-3s8 1 8 3v2h-4V6.5c-1-.5-2.5-.7-4-.7s-3 .2-4 .7V8H2z"/>
            <path d="M5 9h10l2 8H3z"/>
          </svg>
          <span>555.304.2917</span>
        </li>
        <li class="contact-item">
          <svg class="contact-icon" viewBox="0 0 20 20" aria-hidden="true">
            <path d="M2 5h16v1l-8 5-8-5z"/>
            <path d="M2 8l8 5 8-5v8H2z"/>
          </svg>
          <span>marisol@loftplanstudio.example</span>
        </li>
        <li class="contact-item">
          <svg class="contact-icon" viewBox="0 0 20 20" aria-hidden="true">
            <path d="M1 3h18v12H1zm2 2v8h14V5z"/>
            <path d="M7 16h6v2H7z"/>
          </svg>
          <span>www.loftplanstudio.example</span>
        </li>
      </ul>
    </div>
  </div>
</body>
</html>
```